Business Card Design and Basic Text Logo

We are looking for a business card design for an e-business company. Our business is the parent company of a few website businesses. The final logo and business card design will communicate a conservative but modern and expansive business

The Logo text is: 87Merchant
We would also like a basic text logo design for 87Merchant. The logo could also fill up the reverse side of the business card.

The colours we would like to use are:
White
Navy
Black

This is the text that will be added to the card:

Dean Colley
Business Development Manager

Phone: +61 417 658 294
Email: dean.colley@87merchant.com.au

Industry/Entity Type

Business

Logo Text

87Merchant

Logo styles of interest
Pictorial/Combination Logo
Requirements
Must have
• Modern and attractive design
Nice to have
• communicate a conservative but modern and expansive business
Should not have
• Should be too dull and plan
• But also should be overly colourful

```html
<!DOCTYPE html>
<html lang="en">
<head>
<meta charset="utf-8">
<title>87Merchant Business Card</title>
<link rel="stylesheet" href="https://fonts.googleapis.com/css2?family=Didact+Gothic&display=swap">
<style>
  :root {
    --backdrop: #c9c9c9;
    --card-white: #ffffff;
    --navy: #2e3a93;
    --navy-light: #4a56b8;
    --black: #0b0c0e;
    --charcoal: #1c1f24;
    --ink: #16181c;
    --text-light: #f2f2f2;
  }
  * { margin: 0; padding: 0; box-sizing: border-box; }
  html, body {
    width: 1200px;
    height: 900px;
    overflow: hidden;
    background: var(--backdrop);
  }
  .canvas {
    position: relative;
    width: 1200px;
    height: 900px;
    display: flex;
    align-items: center;
    justify-content: center;
    gap: 60px;
  }
  .card {
    position: relative;
    width: 520px;
    height: 300px;
    border-radius: 22px;
    overflow: hidden;
    box-shadow: 0 14px 30px rgba(0, 0, 0, 0.25);
  }
  .wordmark {
    font-family: "Didact Gothic", Arial, sans-serif;
    font-weight: 400;
    letter-spacing: 1px;
    white-space: nowrap;
  }

  /* Front card */
  .card-front { background: var(--card-white); }
  .front-logo-area {
    height: 136px;
    display: flex;
    align-items: center;
    justify-content: center;
  }
  .front-logo-area .wordmark {
    font-size: 44px;
    color: var(--ink);
    margin-top: 16px;
  }
  .accent-band {
    height: 9px;
    background: linear-gradient(90deg, var(--navy), var(--navy-light));
  }
  .contact-panel {
    height: 155px;
    background: radial-gradient(ellipse at 50% 40%, var(--charcoal), var(--black) 80%);
    padding: 14px 26px;
    font-family: "Didact Gothic", Arial, sans-serif;
    color: var(--text-light);
  }
  .person-name {
    font-size: 17px;
    color: var(--navy-light);
    line-height: 1.2;
  }
  .person-title {
    font-size: 13px;
    margin-top: 3px;
  }
  .contact-list {
    list-style: none;
    margin-top: 18px;
    font-size: 16px;
  }
  .contact-list li {
    display: flex;
    align-items: center;
    gap: 8px;
    line-height: 1.35;
  }
  .contact-icon { width: 17px; height: 17px; flex: none; }

  /* Back card */
  .card-back {
    background: radial-gradient(ellipse at 50% 45%, #2a2e35, var(--black) 75%);
    display: flex;
    align-items: center;
    justify-content: center;
  }
  .card-back .wordmark {
    font-size: 52px;
    color: var(--text-light);
  }
</style>
</head>
<body>
<main class="canvas">
  <section class="card card-front" aria-label="Business card front">
    <div class="front-logo-area">
      <span class="wordmark">87Merchant</span>
    </div>
    <div class="accent-band"></div>
    <div class="contact-panel">
      <p class="person-name">Dean Colley</p>
      <p class="person-title">Business Development Manager</p>
      <ul class="contact-list">
        <li>
          <svg class="contact-icon" viewBox="0 0 24 24" aria-hidden="true">
            <path fill="#4a56b8" d="M6.6 10.8a15.1 15.1 0 0 0 6.6 6.6l2.2-2.2c.3-.3.7-.4 1-.2 1.1.4 2.3.6 3.6.6.6 0 1 .4 1 1V20c0 .6-.4 1-1 1A17 17 0 0 1 3 4c0-.6.4-1 1-1h3.5c.6 0 1 .4 1 1 0 1.3.2 2.5.6 3.6.1.3 0 .7-.2 1z"/>
          </svg>
          <span>+61 417 658 294</span>
        </li>
        <li>
          <svg class="contact-icon" viewBox="0 0 24 24" aria-hidden="true">
            <rect x="2" y="5" width="20" height="14" rx="2" fill="#4a56b8"/>
            <path d="M3 6.5l9 6.5 9-6.5" fill="none" stroke="#0b0c0e" stroke-width="1.8"/>
          </svg>
          <span>dean.colley@87merchant.com.au</span>
        </li>
      </ul>
    </div>
  </section>

  <section class="card card-back" aria-label="Business card back">
    <span class="wordmark">87Merchant</span>
  </section>
</main>
</body>
</html>
```